Fold up small biz card size flyer for Waxing Salon

To design a simple informative flyer which can fold 3 times measuring 2" x 9" for Waxing Salon in Toronto ON CanadaMy client would like both sides of flyer to have text i.e. the first half of flyer text on front and second half with address etc on back.She doesn;t want a company name as yet but would like maybe the simple shape of a body as in this sample deisign with a stone background.the other pics are just samples of ideas she has suggessted and if there is any text it should simply be wax or waxing or maybe body waxing.Please don't hesitate to ask quesition and i look forward to your submissions.

Target Market(s)

women amd men of all adult ages

Font styles to use
Serif
Sans Serif
Decorative
Script

Colors

Designer to choose colors to be used in the design.

Requirements
Must have
• Fold into three to biz card size so PLEASE STRICTLY 2 INCHES X 9 INCHES AND FOLDED DOWN TO A 2 X 3 BIZ CARD
• Due to small size of flyer there will have to be text on back as well
• thanks for your time and patience
Nice to have
• the images are simply ideas of existing brands...just stone background with perhadps small body shaped graphic no company name
Should not have
• scanitly clad women preferably small body shoped graphic only please/

```html
<!DOCTYPE html>
<html lang="en">
<head>
<meta charset="utf-8">
<title>Body Waxing – Tri-fold Flyer</title>
<link rel="stylesheet" href="https://fonts.googleapis.com/css2?family=Montserrat:ital,wght@0,400;0,600;0,700;1,400;1,600;1,700&family=Playfair+Display:wght@600&display=swap">
<style>
:root{
  --backdrop:#c4c3c1;
  --paper:#ffffff;
  --rose-dark:#a23a4f;
  --rose-light:#d67794;
  --rose-text:#d45f89;
  --grey-text:#7a7a7c;
  --dark-text:#4a4a4c;
  --stone-tone:rgba(60,58,60,.55);
  --orchid-tone:rgba(236,160,190,.6);
  --pill:#dcdcdc;
}
*{box-sizing:border-box;margin:0;padding:0}
html,body{width:1200px;height:1200px;overflow:hidden}
body{background:var(--backdrop);font-family:"Montserrat",sans-serif;position:relative}
.strip{position:absolute;width:1122px;height:250px;display:flex;background:var(--paper);box-shadow:2px 3px 5px rgba(0,0,0,.25)}
.strip--outside{left:33px;top:307px}
.strip--inside{left:23px;top:610px}
.panel{position:relative;height:100%;overflow:hidden}
.panel--w1{width:369px}.panel--w2{width:377px}.panel--w3{width:376px}
.panel--rose{background:linear-gradient(90deg,var(--rose-dark) 0%,var(--rose-light) 50%,var(--rose-dark) 100%)}
.frame{position:absolute;left:22px;top:22px;right:22px;bottom:22px;border:1px solid var(--rose-light);outline:1px solid var(--rose-light);outline-offset:-4px}
.panel--rose .frame{border-color:rgba(255,255,255,.75);outline-color:rgba(255,255,255,.75)}
.address{position:absolute;left:30px;right:30px;top:34px;text-align:center;font-size:21px;line-height:27px;color:var(--grey-text)}
.panel--rose .address{color:#fff}
.address strong{font-weight:700}
.photo{position:absolute}
.photo--spa{background:linear-gradient(180deg,var(--stone-tone) 0%,var(--orchid-tone) 55%,rgba(236,160,190,0) 100%)}
.photo--spa-right{background:linear-gradient(270deg,var(--orchid-tone) 0%,rgba(236,160,190,0) 100%)}
.photo--spa-top{background:linear-gradient(180deg,var(--stone-tone) 0%,rgba(60,58,60,0) 100%)}
.photo--orchid{background:radial-gradient(ellipse at 80% 80%,var(--orchid-tone),rgba(236,160,190,0) 70%)}
.photo--figure{background:linear-gradient(135deg,rgba(0,0,0,.07),rgba(0,0,0,.01))}
.title-script{position:absolute;left:86px;top:76px;font-family:"Playfair Display",serif;font-weight:600;font-size:38px;color:var(--rose-text);white-space:nowrap}
.deal{position:absolute;left:108px;top:134px;font-weight:700;font-size:27px;line-height:26px;color:var(--grey-text)}
.deal span{color:var(--rose-text)}
.badge{position:absolute;width:72px;height:72px;border-radius:50%;background:linear-gradient(90deg,var(--rose-dark),var(--rose-light) 50%,var(--rose-dark));display:flex;align-items:center;justify-content:center;color:#fff;font-weight:700;font-size:26px}
.badge::after{content:"";position:absolute;inset:4px;border-radius:50%;border:2px dotted rgba(255,255,255,.8)}
.offer-head{position:absolute;font-weight:700;font-size:21px;color:var(--grey-text)}
.offer-body{position:absolute;font-style:italic;font-size:20px;line-height:26px;color:var(--dark-text)}
.offer-body .value{font-style:normal;font-weight:600;color:var(--rose-text)}
.rule{position:absolute;left:50%;transform:translateX(-50%);height:2px;background:#fff;border-radius:2px}
.details{position:absolute;left:24px;right:24px;top:50px;text-align:center;color:#fff;font-style:italic;font-size:20px;line-height:26px}
.details b{font-weight:700}
.cta{position:absolute;left:23px;top:167px;width:292px;height:42px;background:var(--pill);border-radius:8px 0 8px 0}
.cta span{position:absolute;inset:5px;border:2px dotted var(--rose-text);border-radius:6px;display:flex;align-items:center;justify-content:center;font-weight:700;font-style:italic;font-size:19px;color:var(--rose-text)}
</style>
</head>
<body>

<section class="strip strip--outside">
  <div class="panel panel--w1">
    <div class="frame"></div>
    <p class="address"><strong>1520 MAPLE ROW EAST</strong><br>#3&nbsp; Toronto<br>ON&nbsp; M4K 3R8<br>Opp to Saffron Grill<br>House<br><strong>1 (416) 555-0142</strong><br><strong>1 (833) 555-0178</strong></p>
  </div>
  <div class="panel panel--w2 panel--rose">
    <div class="frame"></div>
    <p class="address"><strong>2240 BIRCH PARK AVE</strong><br>#3.&nbsp; North York<br>ON&nbsp; M4A 5T6<br>Opp to Harbour Lane<br>Next to Thrift Mart<br><strong>1 (416) 555-0193</strong><br><strong>1 (833) 555-0116</strong></p>
  </div>
  <div class="panel panel--w3">
    <div class="photo photo--spa" role="img" aria-label="Photo of dark spa stones with pink orchid petals" style="left:0;top:0;width:86px;height:250px"></div>
    <div class="photo photo--spa-top" role="img" aria-label="Photo of dark spa stones" style="left:86px;top:0;width:130px;height:66px"></div>
    <h1 class="title-script">Body Waxing</h1>
    <p class="deal">DOOR<br>BUSTER<br><span>DEAL !</span></p>
    <div class="photo photo--figure" role="img" aria-label="Line drawing of a woman's legs" style="left:214px;top:126px;width:162px;height:120px"></div>
  </div>
</section>

<section class="strip strip--inside">
  <div class="panel panel--w1">
    <div class="photo photo--orchid" role="img" aria-label="Photo of a pink orchid" style="left:250px;top:160px;width:120px;height:90px"></div>
    <div class="badge" style="left:23px;top:35px">$66</div>
    <h2 class="offer-head" style="left:107px;top:38px">BODY WAXING</h2>
    <p class="offer-body" style="left:50px;right:22px;top:63px;text-align:center">
      <span style="display:block;text-align:left;padding-left:54px">For women only</span>
      <span style="display:block;text-align:right">(Neck to Toe — Including</span>
      Brazilian) with Take Home<br>Scrub used to improve<br>in-grown body hair.<br><span class="value">($120 value)</span>
    </p>
  </div>
  <div class="panel panel--w2 panel--rose">
    <div class="rule" style="top:32px;width:180px"></div>
    <p class="details">Guests receive full body wax-<br>ing during one appointment<br>on the following areas: <b>butt,<br>hollywood, bikini, underarms,<br>stomach, cleavage, full back,<br>full arms &amp; full legs.</b></p>
    <div class="rule" style="top:222px;width:180px"></div>
  </div>
  <div class="panel panel--w3">
    <div class="photo photo--spa-top" role="img" aria-label="Photo of dark spa stones" style="left:220px;top:0;width:156px;height:60px"></div>
    <div class="photo photo--spa-right" role="img" aria-label="Photo of a pink orchid" style="left:316px;top:60px;width:60px;height:190px"></div>
    <div class="badge" style="left:23px;top:40px">$66</div>
    <h2 class="offer-head" style="left:101px;top:41px">BODY POLISHING</h2>
    <p class="offer-body" style="left:104px;top:66px">The secret to <b>soft</b>,<br><b>smooth</b> skin.</p>
    <div class="cta"><span>Call today to book a spot.</span></div>
  </div>
</section>

</body>
</html>
```